Info-Flyer-Design für Inserate eines Katalogs von Papeterie- und Bürobedarf
Zielgruppe
KOLBA ist ein Schweizer Grosshandelsunternehmen für Papeterie- und Bürobedarf. Kunden sind ausschliesslich professionelle Wiederverkäufer. Endverbraucher werden nicht direkt, sondern über KOLBA Kunden beliefert.
Das Sortiment umfasst neben Papeterie- und Schulartikeln eine kompetente Auswahl im Bereich Bürobedarf. Die Produktepalette wird laufend weiterentwickelt und umfasst auch den Bereich Catering & Kaffee, Hygiene & Reinigung sowie Betriebssicherheit – alles was im modernen Büro benötigt wird.
KOLBA bietet seinen Kunden umfassende Dienstleistungen an. Diese ermöglichen es, das vom Markt geforderte breite und tiefe Sortiment zielgruppengerecht erfolgreich zu vermarkten und effizient zu verteilen. In enger Zusammenarbeit mit unseren Kunden und Lieferanten entwickeln wir unsere Dienstleistungen stetig weiter. Neben den Vermarktungszielen stehen Effizienzziele, die Doppelspurigkeiten in der Wertschöpfungskette vermeiden, im Vordergrund.
Das oberste Ziel von KOLBA ist es, ein zuverlässiger Partner zu sein. Deshalb geniessen Servicegrad und Lieferqualität höchste Priorität. Wir streben nach kooperativen und langfristigen Geschäftsbeziehungen und setzen neue Technologien zum gemeinsamen Nutzen ein.
Aufgabenstellung
In diesem Auftrag geht es darum, dass wir unseren Lieferanten ein Info Flyer zu senden, damit Sie Inserate in unserem nächsten Katalog für das Jahr 21/22 buchen. Es soll lebendig und erfrischend daher kommen. Das Format soll in A4 erstellt sein. Ich benötige am Ende die Original INDD Dokumente. Der Text kann gem. PDF Vorlage vom letzten Jahr übernommen werden, diesen werden wir selbstständig anpassen. Bitte das Logo in der Anlage verwenden sowie das Titelbild . Schrift haben wir ClanOT. Die Titelbalken (grün) haben wir immer so verwendet, da diese auch im Katalog erscheinen, hier kann aber auch die Farbe geändert werden.

```html
<!DOCTYPE html>
<html lang="de">
<head>
<meta charset="utf-8">
<title>KOLBA Office 20/21 Sortiment – Info-Flyer</title>
<link href="https://fonts.googleapis.com/css2?family=Titillium+Web:wght@300;400;600;700&family=Caveat:wght@400&family=Roboto:wght@300;400&display=swap" rel="stylesheet">
<style>
:root{
  --teal:#8dcfd3;
  --bar:#5a5a5a;
  --ink:#333;
  --paper:#fff;
  --bg:#fff;
  --note:#6b6b6b;
}
*{box-sizing:border-box;margin:0;padding:0}
html,body{width:1200px;height:2355px;overflow:hidden;background:var(--bg)}
body{position:relative;font-family:"Titillium Web",sans-serif;color:var(--ink)}
.page{position:absolute;width:462px;height:666px;background:var(--paper);box-shadow:0 2px 9px rgba(0,0,0,.28);overflow:hidden}
.head{position:absolute;left:0;top:8px;width:453px;height:46px;background:var(--teal);color:#fff}
.head .title{position:absolute;left:26px;top:9px;font-size:20px;line-height:1.3;font-weight:700}
.head .title span{font-weight:300}
.brand{position:absolute;right:16px;top:10px;font-size:19px;font-weight:700;letter-spacing:1px;color:#fff}
.bar{position:absolute;left:0;height:19px;width:170px;background:var(--bar);color:#fff;font-size:9px;font-weight:700;line-height:19px;padding-left:24px}
.txt{position:absolute;font-size:7.6px;line-height:1.32;color:var(--ink)}
.txt p{margin-bottom:6px}
.txt b{font-weight:700}
.ph{position:absolute}
.bullets{list-style:none}
.bullets li{margin-bottom:10px}
.bullets li::before{content:"• "}
.script{font-family:"Caveat",cursive;color:#fff;line-height:1.05}
.note{position:absolute;left:420px;top:2204px;width:190px;text-align:right;font-family:"Roboto",sans-serif;font-weight:300;font-size:17px;line-height:1.3;color:var(--note)}
.dates{position:absolute;font-size:7.6px;line-height:16px;color:#fff}
</style>
</head>
<body>

<!-- Cover -->
<section class="page" style="left:32px;top:24px">
  <div style="position:absolute;left:0;top:0;width:462px;height:124px;background:var(--teal)"></div>
  <div class="brand" style="left:18px;right:auto;top:20px;font-size:24px">KOLBA</div>
  <div style="position:absolute;right:18px;top:12px;text-align:right;color:#fff;line-height:1">
    <div style="font-size:28px;font-weight:700">Office <span style="font-weight:300">Sortiment</span></div>
    <div style="font-size:54px;font-weight:700;margin-top:2px">2020/21</div>
  </div>
  <div class="ph" role="img" aria-label="Titelbild: Schreibtisch von oben mit Laptop, Stiften, Pflanze und Stühlen" style="left:0;top:124px;width:462px;height:542px;background:linear-gradient(160deg,#9c9c9c 0%,#c9c9c9 30%,#ece37b 48%,#ece37b 60%,#8a8a8a 78%,#5f5f5f 100%)"></div>
  <div class="script" style="position:absolute;right:22px;top:570px;font-size:30px;text-align:right">Ein Gesamtpaket, das<br>Erfolg verspricht!</div>
</section>

<!-- Page 2 -->
<section class="page" style="left:617px;top:24px">
  <div class="head"><div class="title">Office 20/21 <span>Sortiment</span></div><div class="brand">KOLBA</div></div>
  <div class="txt" style="left:28px;top:82px;font-size:8.5px"><b>Geschätzte Partner</b></div>
  <div class="txt" style="left:28px;top:100px;width:200px">
    <p>Die Attraktivität und die Nachfrage bestätigt unser Konzept zur Beibehaltung unseres bewährten Office Kataloges in Druckversion.</p>
    <p>Als nach wie vor beliebtes Werbemittel besticht auch die neue Ausgabe mit einem neu überarbeiteten, modernen und ansprechenden Layout, einer umfassenden Auswahl an Artikeln und natürlich dem gewohnten, fachkundigen Inhalt.</p>
  </div>
  <div class="txt" style="left:240px;top:100px;width:200px">
    <p>Lassen Sie sich von unserem Office 19/20 überraschen. Wir streben eine Auflage von 75'000 Exemplaren an.</p>
    <p>Mehr als 250 Fachhändler werden diesen Katalog schweizweit in drei Sprachen zum Einsatz bringen. Der Umfang beträgt wiederum ca. 580 Seiten, die Laufzeit beträgt zwei Jahre.</p>
    <p>Der Office 19/20 wird ab Mitte Dezember 2018 an unsere Fachhändler ausgeliefert.</p>
  </div>
  <div class="bar" style="top:240px;width:172px">Verständliche Katalogübersicht</div>
  <ul class="txt bullets" style="left:28px;top:284px;width:420px">
    <li>Umfangreich und kompetent auf ca. 580 Seiten</li>
    <li>Verkaufsfördernde Anwendungsbilder</li>
    <li>Optimierte und übersichtliche Seitengestaltung</li>
    <li>Zusätzliche Informationen zu Artikelnutzen oder Anwendung</li>
    <li>Piktogramme zur schnelleren Orientierung</li>
    <li>Kaffee, Getränke, Snacks und neue Zusatzsortimente für das Liefergeschäft</li>
  </ul>
  <div class="ph" role="img" aria-label="Aufgeschlagene Katalog-Doppelseite mit Ablagesystemen" style="left:140px;top:425px;width:318px;height:212px;background:linear-gradient(135deg,#e9eef2 0%,#cfd9e2 50%,#f1f1f1 100%)"></div>
  <div class="ph" style="left:0;top:430px;width:140px;height:128px;background:var(--teal)"></div>
  <div class="txt" style="left:22px;top:438px;width:112px;font-size:5.8px;line-height:1.25;color:#fff">
    <p>Eine Platzierung für Logos, Bilder und Piktogramme</p>
    <p>Piktogramme zur Verbesserung der Optik und der Verbindlichkeit</p>
    <p>Verkaufsfördernde Anwendungsbilder</p>
    <p>Hinweis auf Schweizer Qualitätsprodukte</p>
    <p>Tabs zur schnellen Auffindung der Rubriken</p>
  </div>
</section>

<!-- Page 3 -->
<section class="page" style="left:32px;top:726px">
  <div class="head"><div class="title">Office 20/21 <span>Sortiment</span></div><div class="brand">KOLBA</div></div>
  <div class="ph" role="img" aria-label="Foto: Mitarbeiter im Büro mit Ordnern im Hintergrund" style="left:0;top:46px;width:453px;height:324px;background:linear-gradient(120deg,#d7dde0 0%,#a9b4ba 45%,#6f7c85 70%,#c8d0d4 100%)"></div>
  <div class="ph" style="left:200px;top:234px;width:253px;height:327px;background:var(--teal)"></div>
  <div class="script" style="position:absolute;left:215px;top:252px;font-size:26px">Call to action......<br>&nbsp;von Ihnen zu ergänzen</div>
  <div class="bar" style="top:356px">Sortiment</div>
  <div class="txt" style="left:28px;top:392px;width:150px">
    <p>Für den neuen Katalog benötigen wir Ihre Unterstützung. Als Beilage erhalten Sie ein Excelfile mit Ihren gelisteten Artikeln. Bitte prüfen Sie das Sortiment gemäss beiliegender Liste und vermerken Sie, welche Artikel ab Dezember 2018 nicht mehr lieferbar sind. Das überarbeitete Sortiment kann gestaffelt abgegeben werden. Für neu gelistete Katalogartikel erwarten wir ein 100%iges Rückgaberecht bis Ende 2019.</p>
    <p>Damit Sie Ihr Sortiment noch einfacher bearbeiten können, finden Sie auf www.datenablage.ch das PDF des aktuellen Office 19/20 zum Downloaden.</p>
    <p>Benutzername:<br>supplier@kolba_werbung</p>
    <p>Passwort:<br>office1920</p>
  </div>
  <div class="dates" style="left:250px;top:396px">Abgabetermine:</div>
  <div class="dates" style="left:340px;top:396px">
    Kapitel 1: 06.04.2018<br>Kapitel 2: 20.04.2018<br>Kapitel 3: 27.04.2018<br>Kapitel 4: 11.05.2018<br>Kapitel 5: 25.05.2018<br>Kapitel 6: 08.06.2018<br>Kapitel 7: 22.06.2018<br>Kapitel 8: 29.06.2018<br>Kapitel 9: 06.07.2018
  </div>
</section>

<!-- Page 4 -->
<section class="page" style="left:617px;top:726px">
  <div class="head"><div class="title">Office 20/21 <span>Sortiment</span></div><div class="brand">KOLBA</div></div>
  <div class="bar" style="top:75px">Preise Sortiment</div>
  <div class="txt" style="left:28px;top:112px;width:300px">
    <p>Für den Katalog streben wir die aktuellen Preise per 1. Januar 2019 an. Um dies zu gewährleisten, benötigen wir Ihre Preisänderungen bis spätestens Ende August 2018. Später eintreffende Preismutationen können für den Office 19/20 nicht mehr berücksichtigt werden.</p>
    <p>Für das Katalogsortiment akzeptieren wir keine weiteren Preiserhöhungen für das Jahr 2019.</p>
  </div>
  <div class="ph" role="img" aria-label="Foto: Einkaufswagen voller Schreibwaren auf Holztisch" style="left:0;top:232px;width:285px;height:296px;background:linear-gradient(160deg,#cfe1ea 0%,#e8d6a8 55%,#a5774c 100%)"></div>
  <div class="bar" style="left:293px;top:233px;width:169px;padding-left:10px">Fehllieferungen</div>
  <div class="txt" style="left:310px;top:262px;width:140px">
    <p>Entstehen uns durch Fehllieferungen von Katalogartikeln Rückstände, so werden wir Ihnen diese mit CHF 7.50 pro Rückstand verrechnen. Wenn zum Beispiel ein Artikel fehlt und daraus 150 Lieferrückstände an unsere Kunden entstehen, so verrechnen wir Ihnen 150 x CHF 7.50 = CHF 1'125.00.</p>
  </div>
  <div class="bar" style="left:293px;top:417px;width:169px;padding-left:10px">Digitale Mediendaten</div>
  <div class="txt" style="left:310px;top:446px;width:140px">
    <p>Bitte senden Sie uns die Mediendaten ausschliesslich digital (z. B. FileDrop), nicht via CD oder USB Stick.</p>
    <p>Alle weiteren Anforderungen für digitales Bildmaterial entnehmen Sie der separaten Dokumentation Anforderungen Assets.</p>
  </div>
</section>

<!-- Page 5 -->
<section class="page" style="left:32px;top:1439px">
  <div class="head"><div class="title">Office 20/21 <span>Sortiment</span></div><div class="brand">KOLBA</div></div>
  <div class="bar" style="top:75px">Imageseiten</div>
  <div class="txt" style="left:28px;top:104px;width:400px">
    <p>Nutzen Sie die Vorteile der Imageseiten, ausgewählte Produkte werbewirksam auf einer oder mehreren Seiten zu platzieren. Gestalten Sie die Seiten nach Ihren Wünschen, ganz unabhängig vom Kataloglayout.</p>
    <p>Wie bereits erwähnt, wird der Katalog in drei Sprachen produziert, deshalb benötigen wir die Daten separat je in Deutsch, Französisch und Italienisch.</p>
    <p>Bitte senden Sie uns verpackte PageSet Dokumente (inkl. Fonts (Schriften), Links (Bilder) und High End PDFs mit Schnittzeichen). Falls die Daten nicht mit PageSet produziert werden, können Sie uns auch High End PDFs senden.</p>
    <p>Die Daten können Sie uns via Cloud-Dienste (z. B. FileDrop) senden.</p>
  </div>
  <div class="txt" style="left:28px;top:274px;width:400px">
    <p><b>Informationen zum Layout</b><br>Format: 230 x 297 mm + 3 mm Beschnitt (Achtung nicht A4)</p>
  </div>
  <div class="txt" style="left:28px;top:300px"><b>Preise</b><br>Imageseite<br>CHF 2900.00/Seite</div>
  <div class="txt" style="left:198px;top:300px"><b>Abgabetermin</b><br>06.04.2018</div>
  <div class="txt" style="left:28px;top:336px;width:400px">
    <p>Änderungen/Übersetzungen durch KOLBA* ab CHF 129.00/nach Aufwand<br>*sollten die Daten nicht den Anforderungen entsprechen. Die zusätzlich entstandenen Kosten werden direkt verrechnet und sind kein Bestand von WKZ-Vereinbarungen.</p>
  </div>
  <svg class="ph" style="left:28px;top:383px" width="140" height="91" viewBox="0 0 140 91" aria-hidden="true">
    <defs><pattern id="hatch" width="6" height="6" patternUnits="userSpaceOnUse" patternTransform="rotate(45)"><line x1="0" y1="0" x2="0" y2="6" stroke="#c8c8c8" stroke-width="1"/></pattern></defs>
    <rect width="140" height="91" fill="#f2f2f2"/><rect width="70" height="91" fill="url(#hatch)"/>
    <rect x="70" width="70" height="91" fill="#8dcfd3"/>
    <text x="105" y="44" font-size="6" text-anchor="middle" fill="#333" font-family="Titillium Web, sans-serif">230 x 297 mm</text>
    <text x="105" y="52" font-size="6" text-anchor="middle" fill="#333" font-family="Titillium Web, sans-serif">+ 3 mm Beschnitt</text>
  </svg>
  <div class="ph" role="img" aria-label="Beispiel-Imageseite mit Produktraster" style="left:205px;top:383px;width:70px;height:91px;background:linear-gradient(180deg,#f4f4f4,#d9d9d9);border:1px solid #ddd"></div>
  <div class="ph" role="img" aria-label="Beispiel-Imageseite mit Personenfoto" style="left:283px;top:383px;width:70px;height:91px;background:linear-gradient(180deg,#f7f7f7,#e2e6ea);border:1px solid #ddd"></div>
  <div class="ph" role="img" aria-label="Beispiel-Imageseite mit Werbeaktion" style="left:361px;top:383px;width:70px;height:91px;background:linear-gradient(180deg,#efefef,#cfcfcf);border:1px solid #ddd"></div>
  <div class="bar" style="top:545px">Insertionskosten</div>
  <div class="txt" style="left:28px;top:580px;width:400px">
    <p>Für die Einträge werden wir Ihnen pro Seite CHF 2'000.00 in Rechnung stellen.<br>Einzelne Produktegruppen werden anteilsmässig verrechnet.<br>Die Abrechnung erfolgt im Dezember 2018 und betrifft die Ausgabe Office 19/20.</p>
  </div>
</section>

<!-- Page 6 -->
<section class="page" style="left:617px;top:1439px">
  <div class="head"><div class="title">Office 20/21 <span>Sortiment</span></div><div class="brand">KOLBA</div></div>
  <div class="bar" style="top:75px">Termine</div>
</section>

<!-- Page 7 -->
<section class="page" style="left:656px;top:1621px">
  <div class="head"><div class="title">Office 20/21 <span>Sortiment</span></div><div class="brand">KOLBA</div></div>
  <div class="bar" style="top:75px">Kontaktpersonen</div>
  <div class="txt" style="left:28px;top:118px;width:400px">
    <p><b>Sortimentsgestaltung</b><br>Urs Brandli<br>T +41 44 555 01 16<br>urs.brandli@kolba-handel.ch</p>
    <p>Nadja Keller<br>T +41 44 555 01 26<br>nadja.keller@kolba-handel.ch</p>
    <p>Bitte senden Sie sämtliche Vorschläge per E-Mail an nadja.keller@kolba-handel.ch</p>
    <p style="margin-top:12px"><b>Sortimentsdarstellung/Layout</b><br>Corinne Aebi<br>T +41 44 555 02 68<br>corinne.aebi@kolba-handel.ch</p>
    <p style="margin-top:30px">Freundliche Grüsse<br>KOLBA + CO AG</p>
  </div>
  <div class="txt" style="left:28px;top:360px">Urs Brandli<br>Leiter Einkauf</div>
  <div class="txt" style="left:200px;top:360px">Corinne Aebi<br>Leiterin Werbung</div>
</section>

<p class="note">Die letzten beiden Seiten ggf. miteinander kombinieren?</p>

</body>
</html>
```